School Management website

I need page design for our school management system website

Base website is www.brindavo.com. When the student logs in, he will reach the below pages.
You can either design with white and blue background or grey and white background

Page 1 - School Info

Header
product name("Brindavo") in left corner
logout link in right corner

LeftMenu

Dashboard
School Info
School Settings
Staffs
Classes
Messaging
Contact Us

Footer
About link and copyright text

School Info content
The page should have breadcrumb

The content of this page will be the school profile
We have to show the school logo
Name
School Type
School Code
School Count
School Address
School phone 1&2
School Email
School Website

The page content should show edit school profile link which will take the user to another page

```html
<!DOCTYPE html>
<html lang="en">
<head>
<meta charset="utf-8">
<title>Brindavo – School Info</title>
<link href="https://fonts.googleapis.com/css2?family=Arimo:wght@400;700&display=swap" rel="stylesheet">
<style>
  :root {
    --brand-blue: #1e9bfc;
    --text-dark: #1a1a1a;
    --rule: #d9d9d9;
    --logo-border: #cfcfcf;
    --placeholder: #c4c4c4;
    --footer-bg: #484848;
    --white: #ffffff;
  }
  * { box-sizing: border-box; margin: 0; padding: 0; }
  html, body { width: 1200px; height: 1022px; overflow: hidden; }
  body {
    position: relative;
    background: var(--white);
    font-family: "Arimo", Arial, sans-serif;
    color: var(--text-dark);
  }

  /* Header */
  .site-header {
    position: absolute; left: 0; top: 0; width: 1200px; height: 77px;
    background: var(--brand-blue);
  }
  .brand-name {
    position: absolute; left: 19px; top: 12px;
    font-size: 48px; font-weight: 700; color: var(--white); letter-spacing: 0.5px;
  }
  .logout-link {
    position: absolute; right: 12px; top: 10px;
    font-size: 17px; color: var(--white); text-decoration: none;
  }

  /* Breadcrumb */
  .breadcrumb {
    position: absolute; left: 0; top: 77px; width: 1200px; height: 33px;
    border-bottom: 1px solid var(--rule);
    display: flex; align-items: center; padding-left: 13px;
    font-size: 18px;
  }
  .breadcrumb a { color: var(--text-dark); text-decoration: none; }
  .breadcrumb .crumb-sep { width: 12px; height: 14px; margin: 0 22px 0 24px; }

  /* Collapsed side menu tab */
  .menu-tab {
    position: absolute; left: 0; top: 193px; width: 19px; height: 315px;
    background: var(--brand-blue);
    display: flex; align-items: center; justify-content: center;
  }

  /* Content card */
  .profile-card {
    position: absolute; left: 114px; top: 150px; width: 1033px; height: 739px;
    border: 2px solid var(--brand-blue);
  }
  .card-title {
    height: 72px; background: var(--brand-blue); color: var(--white);
    font-size: 36px; font-weight: 400; padding: 16px 0 0 12px; letter-spacing: -0.5px;
  }

  .profile-table {
    position: absolute; left: 70px; top: 94px; width: 650px;
    list-style: none;
  }
  .profile-row {
    display: flex; align-items: center;
    border-bottom: 1px solid var(--rule);
  }
  .profile-row .field-label { width: 156px; flex: none; padding-left: 2px; font-size: 18px; }
  .profile-row .field-value { font-size: 19px; color: var(--brand-blue); white-space: nowrap; }
  .profile-row.is-multiline { align-items: flex-start; padding-top: 6px; }
  .profile-row.is-multiline .field-label { line-height: 38px; }
  .profile-row.is-multiline .field-value { line-height: 38px; }

  .edit-profile-btn {
    position: absolute; left: 570px; top: 617px; width: 152px; height: 42px;
    border: 2px solid var(--brand-blue); background: var(--white);
    display: flex; align-items: center; justify-content: center;
    font-size: 14px; font-weight: 700; color: var(--text-dark); text-decoration: none;
  }

  /* School logo block */
  .school-logo {
    position: absolute; left: 741px; top: 48px; width: 206px; height: 240px;
    background: var(--white); border: 2px solid var(--logo-border);
    display: flex; align-items: center; justify-content: center;
    font-size: 23px; color: var(--placeholder);
  }
  .school-logo-caption {
    position: absolute; left: 741px; top: 298px; width: 206px;
    display: flex; align-items: baseline; justify-content: center; gap: 8px;
    font-size: 18px;
  }
  .school-logo-caption .change-link { font-size: 11px; color: var(--text-dark); text-decoration: none; }

  /* Footer */
  .site-footer {
    position: absolute; left: 0; top: 955px; width: 1200px; height: 67px;
    background: var(--footer-bg); color: var(--white);
    font-size: 14px; font-weight: 700;
  }
  .site-footer .copyright { position: absolute; left: 19px; top: 25px; }
  .footer-contact {
    position: absolute; top: 25px; display: flex; align-items: center; gap: 8px;
  }
  .footer-contact.phone { left: 825px; }
  .footer-contact.email { left: 1002px; }
</style>
</head>
<body>

<header class="site-header">
  <div class="brand-name">Brindavo</div>
  <a class="logout-link" href="#">Logout</a>
</header>

<nav class="breadcrumb" aria-label="Breadcrumb">
  <a href="#">Home</a>
  <svg class="crumb-sep" viewBox="0 0 12 14" aria-hidden="true"><path d="M3 1 L9 7 L3 13" fill="none" stroke="#1a1a1a" stroke-width="1.3"/></svg>
  <span>School info</span>
</nav>

<div class="menu-tab" aria-label="Open menu">
  <svg width="12" height="30" viewBox="0 0 12 30" aria-hidden="true"><path d="M2 3 L10 15 L2 27" fill="none" stroke="#ffffff" stroke-width="1.5"/></svg>
</div>

<main class="profile-card">
  <h1 class="card-title">School Info</h1>

  <ul class="profile-table">
    <li class="profile-row" style="height:48px"><span class="field-label">School Name</span><span class="field-value">Lorem ipsum dolor sit amet, consectetur adipiscing elit</span></li>
    <li class="profile-row" style="height:56px"><span class="field-label">School Type</span><span class="field-value">Praesent vel varius turpis</span></li>
    <li class="profile-row" style="height:52px"><span class="field-label">School Code</span><span class="field-value">001</span></li>
    <li class="profile-row" style="height:48px"><span class="field-label">School Count</span><span class="field-value"></span></li>
    <li class="profile-row is-multiline" style="height:102px"><span class="field-label">School Address</span><span class="field-value">Sed ac orci et lorem sollicitudin viverra phasellus pretium<br>consectetur turpis et gravida dui lacinia sed. Cras</span></li>
    <li class="profile-row" style="height:45px"><span class="field-label">School Phone 1</span><span class="field-value">XXX XXX XXXX</span></li>
    <li class="profile-row" style="height:47px"><span class="field-label">School Phone 2</span><span class="field-value">XXX XXX XXXX</span></li>
    <li class="profile-row" style="height:47px"><span class="field-label">School Email</span><span class="field-value">info@xxxxxx.com</span></li>
    <li class="profile-row" style="height:45px"><span class="field-label">School Website</span><span class="field-value">schoolxxxxxx.com</span></li>
  </ul>

  <a class="edit-profile-btn" href="#">Edit School Profile</a>

  <div class="school-logo" role="img" aria-label="School logo placeholder">Logo</div>
  <div class="school-logo-caption"><span>School Logo</span><a class="change-link" href="#">[Change]</a></div>
</main>

<footer class="site-footer">
  <div class="copyright">Copyright © 2014 | All Rights Reserved</div>
  <div class="footer-contact phone">
    <svg width="14" height="14" viewBox="0 0 24 24" aria-hidden="true"><path fill="#ffffff" d="M6.6 10.8a15.1 15.1 0 0 0 6.6 6.6l2.2-2.2a1 1 0 0 1 1-.25 11.4 11.4 0 0 0 3.6.6 1 1 0 0 1 1 1V20a1 1 0 0 1-1 1A17 17 0 0 1 3 4a1 1 0 0 1 1-1h3.5a1 1 0 0 1 1 1c0 1.25.2 2.45.6 3.6a1 1 0 0 1-.25 1z"/></svg>
    <span>+91 90000 12345</span>
  </div>
  <div class="footer-contact email">
    <svg width="17" height="13" viewBox="0 0 17 13" aria-hidden="true"><rect x="0" y="0" width="17" height="13" rx="1.5" fill="#ffffff"/><path d="M1 1.5 L8.5 7.5 L16 1.5" fill="none" stroke="#484848" stroke-width="1.6"/></svg>
    <span>contact@brindavo.com</span>
  </div>
</footer>

</body>
</html>
```